Flyer design for commercial marketing

Looking to get a flyer design to email out to companies indicating our services
Company Name - Brightwell Networks
Company Logo - (Attached)
Services Offered
FULL HD DIGITAL IP CCTV SYSTEMS
IP ACCESS CONTROL SYSTEMS RFID / BIOMETRIC
IP EMPLOYEE MANAGEMENT SYSTEMS RFID / BIOMETRIC
NETWORKING / FIBER OPTIC SOLUTIONS
The designer can input necessary text and images
It is up to the designer to put images. I dont want the flyer too tacky. I am using this for commercial advertising
Updates
Target Market(s)
Corporate
Industry/Entity Type
It Company
Look and feel
Each slider illustrates characteristics of the customer's brand and the style your logo design should communicate.

```html
<!DOCTYPE html>
<html lang="en">
<head>
<meta charset="utf-8">
<title>Brightwell Networks – Services Flyer</title>
<link rel="stylesheet" href="https://fonts.googleapis.com/css2?family=Oswald:wght@400;700&family=Open+Sans:wght@700&display=swap">
<style>
  :root {
    --orange: #f39a1e;
    --yellow: #f8c52a;
    --blue: #1b6db3;
    --navy: #1d3a6b;
    --ink: #2b2b2b;
    --grey: #4a4a4a;
    --paper: #ffffff;
    --backdrop: #e9e9e9;
  }
  * { margin: 0; padding: 0; box-sizing: border-box; }
  html, body { width: 900px; height: 1200px; overflow: hidden; background: var(--backdrop); }
  .flyer {
    position: relative;
    width: 900px; height: 1200px;
    background: var(--paper);
    overflow: hidden;
    font-family: "Open Sans", Arial, sans-serif;
  }
  .corner-accent { position: absolute; top: 0; right: 0; }
  .brand-mark {
    position: absolute; top: 70px; left: 70px;
    display: flex; align-items: center; gap: 16px;
  }
  .brand-mark .dot {
    width: 70px; height: 70px; border-radius: 50%;
    background: var(--blue);
  }
  .brand-mark .name {
    font-weight: 700; font-size: 26px; color: var(--navy);
  }
  .title-band {
    position: absolute; top: 150px; right: 0;
    width: 420px; height: 120px;
    background: var(--paper);
    border-right: 34px solid var(--orange);
    display: flex; align-items: center; justify-content: flex-end;
    padding-right: 28px;
    box-shadow: -6px 4px 14px rgba(0,0,0,0.12);
  }
  .title-band h1 {
    font-family: "Open Sans", Arial, sans-serif;
    font-weight: 700; font-size: 38px; line-height: 1.15;
    color: var(--navy); text-align: right;
  }
  .photo-area {
    position: absolute; top: 300px; left: 0;
    width: 900px; height: 460px;
    background: linear-gradient(135deg, #0e3f78 0%, #2f7fc4 45%, #c9d6e2 75%, #f2f2f2 100%);
  }
  .swoosh { position: absolute; top: 250px; left: 0; }
  .services-heading {
    position: absolute; top: 770px; left: 40px; right: 40px;
    height: 88px;
    background: linear-gradient(90deg, var(--yellow), var(--orange));
    display: flex; align-items: center; justify-content: center;
  }
  .services-heading h2 {
    font-family: "Oswald", "Arial Narrow", sans-serif;
    font-weight: 700; font-size: 56px; color: var(--ink);
    letter-spacing: 1px;
  }
  .services-list {
    position: absolute; top: 880px; left: 0; right: 0;
    list-style: none; text-align: center;
    font-family: "Oswald", "Arial Narrow", sans-serif;
    font-weight: 400; font-size: 33px; line-height: 56px;
    color: var(--grey); text-transform: uppercase;
  }
  .contact-bar {
    position: absolute; bottom: 40px; left: 40px; right: 40px;
    height: 64px;
    background: var(--orange);
    display: flex; align-items: center; justify-content: space-around;
    font-family: "Oswald", "Arial Narrow", sans-serif;
    font-size: 30px; color: var(--ink);
  }
  .contact-item { display: flex; align-items: center; gap: 14px; }
  .contact-item svg { flex: none; }
</style>
</head>
<body>
<main class="flyer">
  <svg class="corner-accent" width="420" height="160" viewBox="0 0 420 160" aria-hidden="true">
    <path d="M120 0 H420 V150 C330 110 220 60 120 0 Z" fill="var(--orange)"/>
  </svg>

  <div class="brand-mark">
    <span class="dot"></span>
    <span class="name">Brightwell Networks</span>
  </div>

  <div class="title-band">
    <h1>Brightwell<br>Networks</h1>
  </div>

  <div class="photo-area" role="img" aria-label="Photo of a server room with a white IP security camera and a biometric access control keypad"></div>

  <svg class="swoosh" width="900" height="120" viewBox="0 0 900 120" aria-hidden="true">
    <path d="M0 40 C200 -10 420 30 560 50 L560 60 C400 50 200 30 0 90 Z" fill="var(--orange)"/>
    <path d="M0 0 H900 V50 C700 20 560 40 560 50 C420 30 200 -10 0 40 Z" fill="var(--paper)"/>
  </svg>

  <div class="services-heading">
    <h2>Services Offered:</h2>
  </div>

  <ul class="services-list">
    <li>Full HD Digital IP CCTV Systems</li>
    <li>IP Access Control Systems RFID / Biometric</li>
    <li>IP Employee Management Systems RFID / Biometric</li>
    <li>Networking / Fiber Optic Solutions</li>
  </ul>

  <footer class="contact-bar">
    <span class="contact-item">
      <svg width="30" height="30" viewBox="0 0 24 24" aria-hidden="true">
        <circle cx="12" cy="12" r="12" fill="var(--paper)"/>
        <path d="M8.5 5.5l2 3-1.3 1.3c.7 1.6 1.9 2.8 3.5 3.5l1.3-1.3 3 2-1.2 2.2c-4.6-.3-8.9-4.6-9.2-9.2z" fill="var(--ink)"/>
      </svg>
      0198-765-432
    </span>
    <span class="contact-item">
      <svg width="34" height="26" viewBox="0 0 34 26" aria-hidden="true">
        <rect x="1" y="1" width="32" height="24" rx="2" fill="var(--paper)" stroke="var(--ink)" stroke-width="2"/>
        <path d="M2 3 L17 15 L32 3" fill="none" stroke="var(--ink)" stroke-width="2"/>
      </svg>
      www.brightwellnet.com
    </span>
  </footer>
</main>
</body>
</html>
```